High End Art Gallery Business Card

We're looking for a business card design that is elegant and artful. Foil embossing, blind embossed pattern, or some kind of "extra" element to make it stand out. Standard American size. The back should remain blank or nearly blank so that notes can be written on the back.
Please check our website at elsintandor.com to see information about our gallery and the type of artwork that we sell.
Included with the files is a brand identity guideline. In addition to the colors listed, we like to incorporate an indigo blue. The business card design in the guideline seems too simplistic. I have included some photos of other business card designs that have caught my eye.
thank you!

Contact Information for Business Card

Mirela Tandor
Gallery Owner
remaining details are in the attached docs

Requirements
Nice to have
• some kind of natural/organic element to reflect the hand-made nature of all of the original artwork.

```html
<!DOCTYPE html>
<html lang="en">
<head>
<meta charset="utf-8">
<title>Elsin Tandor Gallery — Business Card</title>
<link href="https://fonts.googleapis.com/css2?family=Cinzel:wght@500&family=Arimo:wght@400;700&display=swap" rel="stylesheet">
<style>
  :root {
    --backdrop: #1c1c1e;
    --card: #221d1c;
    --gold: #c9a67a;
    --gold-soft: #8a7050;
    --ink-light: #e6e2dc;
    --rule: #6e6a66;
  }
  * { box-sizing: border-box; margin: 0; padding: 0; }
  html, body {
    width: 1200px; height: 800px; overflow: hidden;
    background: var(--backdrop);
  }
  .sheet {
    position: relative; width: 1200px; height: 800px;
    display: flex; flex-direction: column; align-items: center; justify-content: center;
    gap: 36px;
  }
  .card {
    position: relative; width: 595px; height: 340px;
    background: var(--card); overflow: hidden;
    box-shadow: 0 10px 30px rgba(0,0,0,.45);
  }
  .brand {
    position: absolute; display: flex; flex-direction: column; align-items: center;
    font-family: "Cinzel", serif; color: var(--gold); text-align: center;
  }
  .brand-mark {
    width: 92px; height: 92px; border-radius: 50%;
    border: 3px solid var(--gold); margin-bottom: 16px;
  }
  .brand-name { font-size: 25px; font-weight: 500; letter-spacing: 1px; line-height: 1.1; }
  .brand-tagline { font-size: 10px; font-weight: 500; letter-spacing: 2.4px; margin-top: 8px; }

  /* back of card */
  .card-back .brand { left: 70px; top: 62px; width: 300px; }
  .ornament {
    position: absolute; right: -170px; top: 0; width: 340px; height: 340px; border-radius: 50%;
    background: radial-gradient(circle, #3b3128 0%, #2e2620 55%, var(--gold-soft) 56%, #2a231e 60%, var(--card) 72%);
    opacity: .9;
  }

  /* front of card */
  .card-front .brand { left: 30px; top: 70px; width: 290px; }
  .divider {
    position: absolute; left: 325px; top: 92px; width: 1.5px; height: 160px;
    background: linear-gradient(var(--rule), #b8b4ae, var(--rule));
  }
  .contact {
    position: absolute; left: 352px; top: 98px;
    font-family: "Arimo", sans-serif; color: var(--ink-light);
    font-size: 14px; line-height: 1.3;
  }
  .contact-name { font-weight: 700; font-size: 17px; color: var(--gold); }
  .contact-role { margin-bottom: 14px; }
  .contact-address { margin-bottom: 14px; }
  .contact-line { display: flex; align-items: center; gap: 7px; }
  .contact-line svg { width: 11px; height: 11px; flex: none; }
</style>
</head>
<body>
<main class="sheet">

  <section class="card card-back">
    <div class="brand">
      <div class="brand-mark"></div>
      <div class="brand-name">ELSIN TANDOR GALLERY</div>
      <div class="brand-tagline">FINE ART OF ASIA &amp; THE PACIFIC</div>
    </div>
    <div class="ornament" role="img" aria-label="Gold foil mandala ornament of layered petals"></div>
  </section>

  <section class="card card-front">
    <div class="brand">
      <div class="brand-mark"></div>
      <div class="brand-name">ELSIN TANDOR GALLERY</div>
      <div class="brand-tagline">FINE ART OF ASIA &amp; THE PACIFIC</div>
    </div>
    <div class="divider"></div>
    <div class="contact">
      <div class="contact-name">Mirela Tandor</div>
      <div class="contact-role">Gallery Owner</div>
      <div class="contact-address">417 Kealoha Lane<br>Honolulu, HI 96814</div>
      <div class="contact-line">
        <svg viewBox="0 0 12 12"><path d="M2.5 1h2l1 3-1.3 1a6 6 0 0 0 2.8 2.8L8 6.5l3 1v2c0 .8-.7 1.5-1.5 1.5A8.5 8.5 0 0 1 1 2.5C1 1.7 1.7 1 2.5 1z" fill="var(--gold)"/></svg>
        (808) 555-0142
      </div>
      <div class="contact-line">
        <svg viewBox="0 0 12 12"><path d="M2.5 1h2l1 3-1.3 1a6 6 0 0 0 2.8 2.8L8 6.5l3 1v2c0 .8-.7 1.5-1.5 1.5A8.5 8.5 0 0 1 1 2.5C1 1.7 1.7 1 2.5 1z" fill="var(--gold)"/></svg>
        (808) 555-0187
      </div>
      <div class="contact-line">
        <svg viewBox="0 0 12 12"><rect x="1" y="2.5" width="10" height="7" fill="none" stroke="var(--gold)" stroke-width="1.2"/><path d="M1 2.5l5 4 5-4" fill="none" stroke="var(--gold)" stroke-width="1.2"/></svg>
        info@elsintandor.com
      </div>
      <div class="contact-line">
        <svg viewBox="0 0 12 12"><circle cx="6" cy="6" r="5" fill="none" stroke="var(--gold)" stroke-width="1.2"/><path d="M1 6h10M6 1c-2.5 3-2.5 7 0 10M6 1c2.5 3 2.5 7 0 10" fill="none" stroke="var(--gold)" stroke-width="1"/></svg>
        www.elsintandor.com
      </div>
    </div>
  </section>

</main>
</body>
</html>
```